business card design

We are a company in Hong Kong, distribute & export aquariums and want a new business card. We have added our new fish tank in our new card but do want a better design.
Don't prefer fancy design as this is for export business and need to show overseas office contact.
But do want a professional design and a card that can tell we are in aquatic business.
I will attach a scan copy of current name card, the revised draft we just make, the content to show on name card and the logos
feel free to visit our webpage www.qv-reefhouse.com for more details.

```html
<!DOCTYPE html>
<html lang="en">
<head>
<meta charset="utf-8">
<title>Coral Tide Holding – Business Card</title>
<link rel="stylesheet" href="https://fonts.googleapis.com/css2?family=Arimo:wght@400;700&family=Roboto+Condensed:wght@700&display=swap">
<style>
  :root{
    --bg:#e4e4e4;
    --card:#ffffff;
    --teal:#2f9fb3;
    --teal-dark:#237f91;
    --ink:#3a5560;
    --muted:#7d8a90;
    --strip-bg:#ececec;
    --tank-rim:#2b2f33;
    --tank-water:#f2f5f6;
  }
  *{box-sizing:border-box;margin:0;padding:0}
  html,body{width:1200px;height:960px;overflow:hidden;background:var(--bg);font-family:"Arimo",Arial,sans-serif}
  .stage{width:1200px;height:960px;display:flex;flex-direction:column;align-items:center;justify-content:center;gap:40px}
  .card{position:relative;width:700px;height:420px;background:var(--card);box-shadow:0 6px 18px rgba(0,0,0,.18);overflow:hidden}

  /* front */
  .tank-photo{position:absolute;border-radius:50% / 46%;background:radial-gradient(ellipse at 55% 45%,var(--tank-water) 0 52%,#c9d3d6 62%,var(--tank-rim) 70%);}
  .card-front .tank-photo{left:40px;top:80px;width:290px;height:230px}
  .name{position:absolute;left:360px;top:62px;font-size:40px;font-weight:700;color:var(--teal);letter-spacing:.5px}
  .title{position:absolute;left:420px;top:114px;font-size:14px;color:var(--muted)}
  .contact{position:absolute;left:360px;top:160px;border-collapse:collapse;font-size:13px;color:var(--ink)}
  .contact td{padding:3px 6px 3px 0;vertical-align:top}
  .contact .label{width:70px}
  .contact .sep{width:16px}
  .band{position:absolute;left:0;right:0;bottom:0;height:64px;background:var(--teal)}

  /* back */
  .company{position:absolute;left:22px;top:50%;transform:translateY(-50%) rotate(-90deg);transform-origin:center;white-space:nowrap;
    font-family:"Roboto Condensed","Arial Narrow",sans-serif;font-weight:700;font-size:22px;color:var(--teal);width:0;display:flex;justify-content:center}
  .company span{display:block;white-space:nowrap}
  .badge-strip{position:absolute;left:70px;top:0;bottom:0;width:80px;background:var(--teal);display:flex;flex-direction:column;justify-content:space-around;align-items:center;padding:18px 0}
  .badge{width:58px;height:90px;background:#fff}
  .back-panel{position:absolute;left:150px;top:0;right:0;bottom:0;background:linear-gradient(90deg,var(--strip-bg),#fff 30%)}
  .card-back .tank-photo{left:300px;top:90px;width:300px;height:240px}
</style>
</head>
<body>
<main class="stage">
  <section class="card card-front" aria-label="Business card front">
    <div class="tank-photo" role="img" aria-label="Photo of a round wall-mounted aquarium with goldfish, plants and pebbles"></div>
    <h1 class="name">Mavis Cheung</h1>
    <p class="title">Executive Assistant</p>
    <table class="contact">
      <tr><td class="label">Address</td><td class="sep">:</td><td>G/F, 18 Lotus Lane,<br>Kowloon, Hong Kong</td></tr>
      <tr><td class="label">Phone</td><td class="sep">:</td><td>(852) 2140 5317</td></tr>
      <tr><td class="label">Fax</td><td class="sep">:</td><td>(852) 2140 5318</td></tr>
      <tr><td class="label">Email</td><td class="sep">:</td><td>mavis.cheung@coraltide.com</td></tr>
      <tr><td class="label">Website</td><td class="sep">:</td><td>www.qv-reefhouse.com</td></tr>
    </table>
    <div class="band"></div>
  </section>

  <section class="card card-back" aria-label="Business card back">
    <div class="back-panel"></div>
    <div class="company"><span>CORAL TIDE HOLDING CO.LTD</span></div>
    <div class="badge-strip">
      <div class="badge"></div>
      <div class="badge"></div>
      <div class="badge"></div>
    </div>
    <div class="tank-photo" role="img" aria-label="Photo of a round wall-mounted aquarium with goldfish, plants and pebbles"></div>
  </section>
</main>
</body>
</html>
```